Funeral Comparison Website Needs Designer For WireFrame Mock Up (That we've already done)

This should be a pretty quick design project. It's a single page based on a wireframe mockup we did.
Our site (restfulpathway.example) helps people find and compare funeral homes and cemeteries. Our site hasn't been redesigned since we launched in 2008, so it is fairly dated, and we've seen new competitors pop-up in the past year so we need to come up with a fresh redeisgn. We need someone to take our mockup and work their magic with it. As I mentioned this is a single page based on our wireframe mockup.
Please see attached mockup and logo.
Look and feel
Each slider illustrates characteristics of the customer's brand and the style your logo design should communicate.

```html
<!DOCTYPE html>
<html lang="en">
<head>
<meta charset="utf-8">
<title>RestfulPathway – Request Funeral Quotes</title>
<link href="https://fonts.googleapis.com/css2?family=Open+Sans:wght@400;600;700&display=swap" rel="stylesheet">
<style>
  :root{
    --ink:#333333;
    --muted:#8a8a8a;
    --brand-blue:#1d84b8;
    --brand-green:#3aa935;
    --link-blue:#2a7fc1;
    --link-green:#4fa531;
    --sky-top:#2f73b6;
    --sky-mid:#4a96d2;
    --sky-low:#8fc3e6;
    --dark:#2b2b2b;
    --dark-box:#333333;
    --band-light:#f3f3f3;
    --band-grey:#e4e4e4;
    --green-top:#4cbf2c;
    --green-bottom:#2f9a1b;
    --footer-bar:#2f74b4;
    --quote-blue:#8ec7e6;
    --white:#ffffff;
  }
  *{box-sizing:border-box;margin:0;padding:0}
  html,body{width:1056px;height:1200px;overflow:hidden}
  body{position:relative;font-family:"Open Sans",Arial,sans-serif;color:var(--ink);background:var(--band-light)}
  .abs{position:absolute}

  /* header */
  .site-header{left:0;top:0;width:1056px;height:115px;background:linear-gradient(#ffffff,#f1f1f1);border-bottom:1px solid #d8d8d8}
  .brand{left:97px;top:46px;display:flex;align-items:center;gap:10px}
  .brand-dot{width:22px;height:22px;border-radius:50%;background:var(--brand-green)}
  .brand-name{font-size:34px;font-weight:600;color:var(--brand-blue);letter-spacing:-0.5px;line-height:1}
  .contact{right:129px;top:14px;text-align:right}
  .contact-phone{font-size:29px;color:#4a4a4a;line-height:1.1}
  .contact-email{font-size:13px;color:var(--link-blue)}
  .main-nav{left:424px;top:88px;display:flex;font-size:15px;color:#333}
  .main-nav span{padding:0 12px;border-left:1px solid #bdbdbd;line-height:20px}
  .main-nav span:first-child{border-left:none}

  /* hero */
  .hero{left:0;top:115px;width:1056px;height:265px;background:linear-gradient(180deg,var(--sky-top) 0%,var(--sky-mid) 55%,var(--sky-low) 88%,#5d8fae 91%,#4f7e9c 100%)}
  .hero-sky{left:0;top:0;width:100%;height:100%;background:radial-gradient(ellipse 260px 140px at 960px 40px,rgba(255,255,255,.45),transparent 70%),radial-gradient(ellipse 300px 60px at 120px 230px,rgba(255,255,255,.35),transparent 70%)}
  .hero-title{left:0;top:34px;width:1030px;text-align:center;font-size:48px;font-weight:700;color:var(--white);text-shadow:0 2px 4px rgba(0,0,0,.3)}
  .hero-sub{left:0;top:97px;width:1030px;text-align:center;font-size:21px;color:var(--white)}
  .hero-call{left:0;top:128px;width:1030px;text-align:center;font-size:27px;color:var(--white)}
  .path-btn{top:204px;width:277px;height:60px;background:var(--dark-box);border-radius:3px 3px 0 0;display:flex;align-items:center;gap:10px;padding:0 16px 0 12px;color:var(--white);font-size:16px;line-height:1.25}
  .path-btn .label{flex:1;text-align:center;white-space:nowrap}
  .path-btn svg{width:38px;height:38px;flex:none}

  .primary-btn{left:409px;top:409px;width:237px;height:50px;border-radius:5px;background:linear-gradient(var(--green-top),var(--green-bottom));color:var(--white);font-size:20px;display:flex;align-items:center;padding-left:22px;box-shadow:0 1px 2px rgba(0,0,0,.3)}
  .primary-btn svg{position:absolute;right:14px;top:12px;width:26px;height:26px}
  .primary-btn::after{content:"";position:absolute;right:54px;top:0;width:1px;height:50px;background:rgba(255,255,255,.25)}

  /* testimonials */
  .testimonial-band{left:0;top:450px}
  .resources-tab{left:764px;top:487px;width:204px;height:35px;background:var(--white);border-radius:0 0 6px 6px;display:flex;align-items:center;gap:10px;padding-left:10px;font-size:14px;font-weight:700;color:#222;box-shadow:0 1px 3px rgba(0,0,0,.3)}
  .resources-tab svg{width:22px;height:22px}
  .section-title{left:0;top:496px;width:1050px;text-align:center;font-size:35px;font-weight:400;color:var(--white)}
  .section-sub{left:0;top:543px;width:1050px;text-align:center;font-size:12px;font-weight:700;color:var(--white)}
  .testimonial{top:575px;width:281px;height:190px;background:var(--white);padding:28px 20px 0 22px;font-size:13px;line-height:21px;color:#333;box-shadow:0 1px 3px rgba(0,0,0,.25)}
  .testimonial .quote-mark{position:absolute;left:10px;top:6px;font-size:58px;line-height:1;height:30px;overflow:hidden;font-weight:700;color:var(--quote-blue);font-family:Georgia,serif}
  .testimonial p{text-indent:20px}
  .testimonial .author{position:absolute;right:18px;top:140px;text-align:right;font-size:13px;line-height:19px;font-weight:700}
  .testimonial .author span{display:block;font-weight:400;color:#9a9a9a}
  .testimonial .tail{position:absolute;left:37px;bottom:-28px;width:0;height:0;border-top:28px solid var(--white);border-left:20px solid transparent}
  .avatar{top:765px;width:94px;height:94px;border-radius:50%;background:var(--white);box-shadow:0 1px 4px rgba(0,0,0,.3);padding:4px}
  .avatar div{width:100%;height:100%;border-radius:50%;background:linear-gradient(#f7f7f7,#dcdcdc)}

  .support-band{left:0;top:733px;width:1056px;height:195px;background:var(--band-grey);border-bottom:1px solid #c9c9c9}
  .support-title{left:0;top:880px;width:1042px;text-align:center;font-size:21px;font-weight:400;color:#333}

  .help-area{left:0;top:928px;width:1056px;height:214px;background:#f4f4f4}
  .help-col{top:958px;width:290px;text-align:center;color:#333}
  .help-col h2{font-size:22px;font-weight:400;line-height:30px}
  .help-col p{font-size:15px;line-height:23px}
  .divider{top:970px;width:1px;height:120px;background:#dcdcdc}
  .more-btn{top:1079px;width:191px;height:40px;border-radius:3px;background:linear-gradient(var(--green-top),var(--green-bottom));color:var(--white);font-size:16px;display:flex;align-items:center;padding-left:16px;box-shadow:0 1px 2px rgba(0,0,0,.3)}
  .more-btn svg{position:absolute;right:10px;top:8px;width:24px;height:24px}

  .footer-bar{left:0;top:1142px;width:1056px;height:21px;background:var(--footer-bar)}
  .site-footer{left:0;top:1163px;width:1056px;height:37px;background:#f4f4f4;text-align:center;font-size:13px;line-height:37px;color:#222}
  .site-footer .link{color:var(--link-blue)}
  .site-footer .partner{color:var(--link-green)}
</style>
</head>
<body>
<svg width="0" height="0" class="abs" aria-hidden="true">
  <symbol id="arrow-white" viewBox="0 0 40 40">
    <circle cx="20" cy="20" r="19" fill="#fff"/>
    <path d="M10 20h16M19 12l8 8-8 8" stroke="#2b2b2b" stroke-width="4.5" fill="none" stroke-linecap="round" stroke-linejoin="round"/>
  </symbol>
  <symbol id="arrow-green" viewBox="0 0 40 40">
    <circle cx="20" cy="20" r="19" fill="#fff"/>
    <path d="M10 20h16M19 12l8 8-8 8" stroke="#2f9a1b" stroke-width="4.5" fill="none" stroke-linecap="round" stroke-linejoin="round"/>
  </symbol>
</svg>

<header class="abs site-header">
  <div class="abs brand"><span class="brand-dot"></span><span class="brand-name">RestfulPathway</span></div>
  <div class="abs contact">
    <div class="contact-phone">800-555-0142</div>
    <div class="contact-email">info@restfulpathway.example</div>
  </div>
  <nav class="abs main-nav"><span>Home</span><span>How It Works</span><span>About Us</span><span>Contact Us</span><span>Resources</span></nav>
</header>

<section class="abs hero">
  <div class="abs hero-sky" role="img" aria-label="Blue sky with soft white clouds"></div>
  <h1 class="abs hero-title">Request Funeral Quotes</h1>
  <div class="abs hero-sub">Free no obligations prices &amp; service quotes</div>
  <div class="abs hero-call">Give us a call 800-555-0142</div>
  <div class="abs path-btn" style="left:96px"><span class="label">I am planning for the<br>long term future</span><svg><use href="#arrow-white"/></svg></div>
  <div class="abs path-btn" style="left:389px"><span class="label">I am planning for a death<br>that will occur shortly</span><svg><use href="#arrow-white"/></svg></div>
  <div class="abs path-btn" style="left:681px"><span class="label">A death has just occured</span><svg><use href="#arrow-white"/></svg></div>
</section>

<div class="abs primary-btn">How it works<svg><use href="#arrow-green"/></svg></div>

<svg class="abs testimonial-band" width="1056" height="290" viewBox="0 0 1056 290" aria-hidden="true">
  <defs>
    <linearGradient id="band-dark" x1="0" y1="0" x2="0" y2="1">
      <stop offset="0" stop-color="#3a3a3a"/><stop offset="1" stop-color="#1f1f1f"/>
    </linearGradient>
  </defs>
  <path d="M0 52 Q528 10 1056 52 L1056 283 L0 283 Z" fill="#555"/>
  <path d="M0 58 Q528 16 1056 58 L1056 283 L0 283 Z" fill="url(#band-dark)"/>
</svg>
<div class="abs resources-tab">
  <svg viewBox="0 0 22 22"><circle cx="11" cy="11" r="11" fill="#222"/><path d="M11 5v10M6.5 11l4.5 4.5 4.5-4.5" stroke="#fff" stroke-width="2.6" fill="none" stroke-linecap="round" stroke-linejoin="round"/></svg>
  Additional resources
</div>
<h2 class="abs section-title">Testimonials</h2>
<div class="abs section-sub">see what out customer have to say</div>

<div class="abs support-band"></div>

<article class="abs testimonial" style="left:97px">
  <span class="quote-mark">“</span>
  <p>Lorem ipsum dolor sit amet, con-sectetur adipiscing elit. Fusce eros sem, scelerisque eget tempus quis, hendrerit id dui. Nam quis varius velit. Ut sed risus mi, vel ultrices nibh.</p>
  <div class="author">- Sam Porter<span>Cambridge</span></div>
  <span class="tail"></span>
</article>
<article class="abs testimonial" style="left:389px">
  <span class="quote-mark">“</span>
  <p>Lorem ipsum dolor sit amet, con-sectetur adipiscing elit. Fusce eros sem, scelerisque eget tempus quis, hendrerit id dui. Nam quis varius velit. Ut sed risus mi, vel ultrices nibh.</p>
  <div class="author">- Sam Porter<span>Cambridge</span></div>
  <span class="tail"></span>
</article>
<article class="abs testimonial" style="left:681px">
  <span class="quote-mark">“</span>
  <p>Lorem ipsum dolor sit amet, con-sectetur adipiscing elit. Fusce eros sem, scelerisque eget tempus quis, hendrerit id dui. Nam quis varius velit. Ut sed risus mi, vel ultrices nibh.</p>
  <div class="author">- Sam Porter<span>Cambridge</span></div>
  <span class="tail"></span>
</article>

<div class="abs avatar" style="left:184px"><div role="img" aria-label="Customer profile photo placeholder"></div></div>
<div class="abs avatar" style="left:474px"><div role="img" aria-label="Customer profile photo placeholder"></div></div>
<div class="abs avatar" style="left:767px"><div role="img" aria-label="Customer profile photo placeholder"></div></div>

<h2 class="abs support-title">Support Centre</h2>

<section class="abs help-area"></section>
<div class="abs help-col" style="left:87px;top:958px">
  <h2>Questions &amp; Answers</h2>
  <p>-how we help<br>- how this works<br>....</p>
</div>
<div class="abs divider" style="left:383px"></div>
<div class="abs help-col" style="left:385px;top:958px">
  <h2>Resources</h2>
  <p>-advice<br>- finances<br>- planning guides</p>
</div>
<div class="abs divider" style="left:676px"></div>
<div class="abs help-col" style="left:676px;top:966px">
  <h2>Get more Help</h2>
  <p>-learn about our<br>certified consultants<br>....</p>
</div>
<div class="abs more-btn" style="left:135px">More Information<svg><use href="#arrow-green"/></svg></div>
<div class="abs more-btn" style="left:438px">More Information<svg><use href="#arrow-green"/></svg></div>
<div class="abs more-btn" style="left:731px">More Information<svg><use href="#arrow-green"/></svg></div>

<div class="abs footer-bar"></div>
<footer class="abs site-footer">
  © 2008-2013 RestfulPathway.example. All Rights Reserved. <span class="link">Privacy Policy</span> | <span class="link">Contact Us</span> | <span class="link">Home</span> | <span class="partner">Partner with Restful Pathway</span>
</footer>
</body>
</html>
```